" Trabalho de forma autônoma como Coach Executivo. O Coaching executivo pode ser contratado tanto por PJ como por PF. São sessões / reuniões nas quais trabalhamos de forma individual para desenvolvimento da pessoa - desenvolvimento de habilidades, autoconsciência dos pontos fortes e pontos a serem desenvolvidos, para que a pessoa desempenhe seu máximo em sua carreira profissional e atinja o sucesso que ela determinou. O foco do trabalho é o desenvolvimento de competências / habilidades para ela desempenhar seu trabalho e se desenvolver em sua carreira profissional com excelência. Também tem o foco, no Coaching de Carreira, na redefinição dos rumos profissionais de uma pessoa. Discussão de possibilidades de caminhos a serem seguidos e uma reflexão do que aconteceu até o momento. Em ambos os casos, é um processo de autoreflexão mas que já parte para a AÇÃO. Não tem nada de estático, só ficar pensando e divagando em ideias. O ponto é fazer com que a pessoa se mova, saia do lugar, vá buscar seus objetivos. Esse apoio durante o processo também é dado para que a ação efetivamente aconteça. "

```html
<!DOCTYPE html>
<html lang="pt-BR">
<head>
<meta charset="UTF-8">
<title>Assinatura de e-mail — Marina Toledo Coaching</title>
<link rel="stylesheet" href="https://fonts.googleapis.com/css2?family=Raleway:wght@300;400;500&display=swap">
<style>
  :root {
    --page-bg: #eef0ef;
    --banner: #2e3032;
    --banner-edge: #3a3d40;
    --ink-light: #f2f2f2;
    --ink-soft: #c9cccd;
    --accent: #6fb3a8;
    --divider: #d9d9d9;
  }
  * { margin: 0; padding: 0; box-sizing: border-box; }
  html, body {
    width: 1200px; height: 1200px; overflow: hidden;
    background: var(--page-bg);
    font-family: "Raleway", Arial, sans-serif;
  }
  .signature {
    position: absolute;
    left: 100px; top: 435px;
    width: 1000px; height: 330px;
  }
  .signature-shape { position: absolute; inset: 0; }
  .brand {
    position: absolute;
    left: 60px; top: 0; width: 340px; height: 330px;
    display: flex; flex-direction: column; justify-content: center; align-items: center;
    gap: 14px;
  }
  .brand-mark {
    width: 58px; height: 58px; border-radius: 50%;
    background: var(--accent);
  }
  .brand-name {
    font-weight: 300; font-size: 40px; letter-spacing: 3px;
    color: var(--ink-light); white-space: nowrap;
  }
  .brand-tagline {
    font-weight: 400; font-size: 15px; letter-spacing: 8px;
    color: var(--ink-soft);
  }
  .divider {
    position: absolute; left: 450px; top: 60px;
    width: 2px; height: 210px; background: var(--divider);
  }
  .contacts {
    position: absolute; left: 490px; top: 62px; width: 450px;
    list-style: none; display: flex; flex-direction: column; gap: 34px;
  }
  .contact {
    display: flex; align-items: center; justify-content: space-between;
    color: var(--ink-light); font-size: 24px; font-weight: 400;
    height: 34px;
  }
  .contact-icon { width: 26px; height: 26px; flex: none; }
  .contact-icon--dot { width: 20px; height: 20px; border-radius: 3px; background: var(--ink-light); margin-right: 3px; }
</style>
</head>
<body>
  <section class="signature" aria-label="Assinatura de e-mail">
    <svg class="signature-shape" width="1000" height="330" viewBox="0 0 1000 330" aria-hidden="true">
      <path d="M0 0 H985 Q1000 0 1000 15 V190 Q1000 330 860 330 H0 Z" fill="var(--banner)"/>
      <path d="M0 0 H985 Q1000 0 1000 15 V190 Q1000 330 860 330 H0 Z" fill="none" stroke="var(--banner-edge)" stroke-width="2"/>
    </svg>

    <div class="brand">
      <span class="brand-mark"></span>
      <span class="brand-name">MARINA TOLEDO</span>
      <span class="brand-tagline">COACHING</span>
    </div>

    <span class="divider"></span>

    <ul class="contacts">
      <li class="contact">
        <span>contato@marinatoledo.com.br</span>
        <svg class="contact-icon" viewBox="0 0 24 24" aria-label="e-mail">
          <rect x="2" y="5" width="20" height="14" rx="1.5" fill="var(--ink-light)"/>
          <path d="M3 6 L12 13 L21 6" fill="none" stroke="var(--banner)" stroke-width="1.8"/>
        </svg>
      </li>
      <li class="contact">
        <span>11 98765-4321</span>
        <svg class="contact-icon" viewBox="0 0 24 24" aria-label="telefone">
          <path d="M6.6 3 L9.5 6.4 L7.8 9 C9 11.6 12.4 15 15 16.2 L17.6 14.5 L21 17.4 L19.3 20.6 C11.5 20.6 3.4 12.5 3.4 4.7 Z" fill="var(--ink-light)"/>
        </svg>
      </li>
      <li class="contact">
        <span>perfil.exemplo.com/marina-toledo</span>
        <span class="contact-icon contact-icon--dot" aria-label="perfil profissional"></span>
      </li>
    </ul>
  </section>
</body>
</html>
```